Bread Baking Blog

I need theme modification/customization and logo for a Wordpress theme that I can use the blog about bread baking. Needs to include pictures & recipes.

Can provide access to my quillpage.com site. Have paid for https://plankvault.com/themes/brisk/ but open to alternatives.

The site name is "crumb42.com" (Crumb 42 flour is a type of bread flour used in artisan bread baking). Not particular on color palette - am looking for your creativity.

I've included some logos for other domains I have to help provide some inspiration.

```html
<!DOCTYPE html>
<html lang="en">
<head>
<meta charset="utf-8">
<title>Crumb 42. For Bakers</title>
<link rel="stylesheet" href="https://fonts.googleapis.com/css2?family=Montserrat:wght@400;500;600;700&family=Mulish:wght@300;400;500&display=swap">
<style>
:root{
  --green:#5b8a0e;
  --green-dark:#4c7509;
  --ink:#2e2e2e;
  --text:#444;
  --muted:#777;
  --gold:#c99a1c;
  --welcome-bg:#eef3fa;
  --recipes-bg:#f6f8fc;
  --footer-bg:#f7efd6;
  --rule:#dcdfe4;
  --white:#fff;
}
*{box-sizing:border-box;margin:0;padding:0}
html,body{width:1200px;height:3469px;overflow:hidden}
body{font-family:"Mulish",sans-serif;color:var(--text);background:var(--white);position:relative}
.btn{display:inline-flex;align-items:center;gap:8px;background:var(--green);color:var(--white);font-family:"Mulish",sans-serif;font-size:18px;text-decoration:none;padding:0 18px;height:40px}
.btn .dot{width:14px;height:14px;border-radius:50%;background:var(--white);display:inline-flex;align-items:center;justify-content:center}
.btn .dot svg{display:block}

/* header */
.site-header{position:absolute;top:0;left:0;width:1200px;height:112px;background:var(--white)}
.brand{position:absolute;left:130px;top:44px;display:flex;align-items:center;gap:10px;font-family:"Montserrat",sans-serif;font-weight:700;font-size:22px;color:var(--gold);letter-spacing:.5px}
.brand .mark{width:26px;height:26px;border-radius:50%;background:var(--gold)}
.topbar{position:absolute;right:120px;top:22px;display:flex;align-items:center;gap:12px;font-family:"Montserrat",sans-serif;font-size:19px;color:var(--ink)}
.social{display:flex;gap:12px;margin-left:14px}
.social span{width:14px;height:14px;border-radius:50%;background:var(--green)}
.main-nav{position:absolute;right:120px;top:70px;display:flex;gap:60px;font-family:"Montserrat",sans-serif;font-size:19px}
.main-nav a{color:var(--ink);text-decoration:none}
.main-nav a.active{color:var(--green);text-decoration:underline;text-underline-offset:5px}

/* hero */
.hero{position:absolute;top:112px;left:0;width:1200px;height:583px;background:linear-gradient(100deg,#3a1c0c 0%,#7a3d16 35%,#a5581f 60%,#5a2a10 100%)}
.hero-band{position:absolute;top:695px;left:0;width:1200px;height:10px;background:var(--green);border-bottom:3px solid #fff}
.hero-copy{position:absolute;left:118px;top:255px;color:var(--white)}
.hero-copy h1{font-family:"Montserrat",sans-serif;font-weight:700;font-size:54px;line-height:1.1}
.hero-copy p{font-family:"Montserrat",sans-serif;font-weight:500;font-size:19px;line-height:29px;margin-top:14px;width:480px}
.hero-copy .btn{margin-top:44px;margin-left:4px;height:48px;padding:0 24px;font-size:19px;border:2px solid #6f9c25;opacity:.92}

/* welcome */
.welcome{position:absolute;top:705px;left:0;width:1200px;height:458px;background:var(--welcome-bg)}
.welcome h2{position:absolute;left:130px;top:72px;font-family:"Mulish",sans-serif;font-weight:400;font-size:38px;color:var(--ink);letter-spacing:-.5px}
.welcome .copy{position:absolute;left:130px;top:130px;width:500px;font-size:15.5px;line-height:29px;font-weight:300;color:var(--ink)}
.welcome .copy p+p{margin-top:11px}
.welcome .btn{position:absolute;left:130px;top:351px;height:42px;padding:0 14px}
.welcome .photo{position:absolute;left:731px;top:80px;width:348px;height:242px;background:linear-gradient(135deg,#f3f0ea 0%,#e8c99a 45%,#f1ede7 100%);box-shadow:0 6px 16px rgba(0,0,0,.12)}

/* recipes */
.recipes{position:absolute;top:1163px;left:0;width:1200px;height:1997px;background:var(--recipes-bg)}
.recipes h2{position:absolute;left:118px;top:42px;font-family:"Mulish",sans-serif;font-weight:400;font-size:41px;color:#555}
.recipes h2 em{font-style:normal;color:var(--green)}
.recipes .rule{position:absolute;left:118px;top:117px;width:962px;height:1px;background:var(--rule)}
.recipe-grid{position:absolute;left:121px;top:162px;display:grid;grid-template-columns:455px 455px;column-gap:49px;row-gap:49px}
.recipe-card{height:530px;background:var(--white);box-shadow:0 0 8px rgba(0,0,0,.08);padding:8px;position:relative}
.recipe-card .photo{height:239px;border-radius:3px}
.recipe-card .meta{display:flex;justify-content:space-between;margin:33px 18px 0;font-size:13px;font-weight:300;color:var(--muted)}
.recipe-card h3{margin:14px 18px 0;font-family:"Mulish",sans-serif;font-weight:500;font-size:16.5px;line-height:27px;color:var(--ink)}
.recipe-card p{margin:10px 18px 0;font-size:14px;font-weight:300;line-height:24px;color:#555}
.recipe-card .btn{position:absolute;left:24px;top:460px;height:38px;font-size:17px}
.p1{background:linear-gradient(120deg,#e9eaea,#d79a3c 55%,#c6b79f)}
.p2{background:linear-gradient(120deg,#2b2a2a 30%,#d9c3a2 70%,#8a6d50)}
.p3{background:linear-gradient(120deg,#8c7b6d,#e3dcd6 50%,#b7a99a)}
.p4{background:linear-gradient(120deg,#d9d9d9,#c77a4c 50%,#ebe7e2)}
.p5{background:linear-gradient(120deg,#9d7652,#3d6f64 45%,#e8b240 80%)}
.p6{background:linear-gradient(120deg,#6b3b22,#b35a2a 50%,#2d3e5a)}
.recipes .more{position:absolute;left:511px;top:1902px;height:42px;padding:0 12px}

/* footer */
.site-footer{position:absolute;top:3160px;left:0;width:1200px;height:309px;background:var(--footer-bg);font-family:"Montserrat",sans-serif;color:#555}
.site-footer h4{font-weight:500;font-size:14px;color:#444;margin-bottom:14px}
.fcol{position:absolute;top:56px}
.fcol a{display:block;font-size:13.5px;color:#666;text-decoration:none;line-height:24px}
.contact h4{font-size:17px;font-weight:400;margin-bottom:12px}
.contact li{list-style:none;display:flex;gap:10px;font-size:15px;line-height:21px;margin-bottom:14px}
.contact svg{flex:none;margin-top:3px}
.newsletter p{font-size:13.5px;line-height:21px;width:210px;color:#666}
.subscribe{display:flex;margin-top:22px;width:258px;height:34px}
.subscribe span{flex:1;background:var(--white);border-radius:17px 0 0 17px;font-size:12px;color:#999;padding:10px 22px}
.subscribe b{width:108px;background:var(--green);color:var(--white);border-radius:0 17px 17px 0;font-size:13px;font-weight:600;display:flex;align-items:center;justify-content:center}
.footer-rule{position:absolute;left:0;top:230px;width:1200px;height:1px;background:#e3d9bb}
.copyright{position:absolute;left:112px;top:262px;font-size:16px;color:#555}
.site-footer .social{position:absolute;right:135px;top:266px}
</style>
</head>
<body>

<header class="site-header">
  <div class="brand"><span class="mark"></span>CRUMB 42</div>
  <div class="topbar">
    <svg width="22" height="15" viewBox="0 0 22 15"><rect width="22" height="15" fill="#5b8a0e"/><path d="M0 0l11 8 11-8" fill="none" stroke="#fff" stroke-width="1.6"/></svg>
    info@companyname.com
    <div class="social"><span></span><span></span><span></span></div>
  </div>
  <nav class="main-nav">
    <a class="active" href="#">Home</a><a href="#">About Us</a><a href="#">Recipes</a><a href="#">Contact Us</a>
  </nav>
</header>

<section class="hero" role="img" aria-label="Rustic breads, baguettes and a wicker basket on a dark wooden table"></section>
<div class="hero-copy">
  <h1>Crumb 42. For Bakers</h1>
  <p>Lorem Ipsum is simply dummy text of the printing and typesetting industry</p>
  <a class="btn" href="#">Explore Now!</a>
</div>
<div class="hero-band"></div>

<section class="welcome">
  <h2>Welcome to Crumb 42. For Bakers.</h2>
  <div class="copy">
    <p>Lorem Ipsum is simply dummy text of the printing and typesetting industry. Lorem Ipsum has been the industry's standard dummy text ever since the 1500s</p>
    <p>Lorem Ipsum is simply dummy text of the printing and typesetting industry. Lorem Ipsum has been the industry's standard dummy text ever since the 1500s Lorem Ipsum is simply dummy text</p>
  </div>
  <a class="btn" href="#">Learn More <span class="dot"><svg width="8" height="8" viewBox="0 0 8 8"><path d="M2.5 1l3 3-3 3" fill="none" stroke="#5b8a0e" stroke-width="1.6"/></svg></span></a>
  <div class="photo" role="img" aria-label="Breakfast spread with croissants, fruit, juice and coffee on a marble top"></div>
</section>

<section class="recipes">
  <h2>Latest <em>Recipes</em></h2>
  <div class="rule"></div>
  <div class="recipe-grid">
    <article class="recipe-card"><div class="photo p1" role="img" aria-label="Braided pastry with spices, rowan berries and apples"></div><div class="meta"><span>By: Auther Name</span><span>2 Comments</span></div><h3>Lorem Ipsum is simply dummy text of the printing and typesetting industry.</h3><p>Lorem Ipsum is simply dummy text of the printing and typesetting industry. Lorem Ipsum has been the industry's standard dummy text</p><a class="btn" href="#">Read More</a></article>
    <article class="recipe-card"><div class="photo p2" role="img" aria-label="Toast, fried egg and bacon on a plate on a dark table"></div><div class="meta"><span>By: Auther Name</span><span>2 Comments</span></div><h3>Lorem Ipsum is simply dummy text of the printing and typesetting industry.</h3><p>Lorem Ipsum is simply dummy text of the printing and typesetting industry. Lorem Ipsum has been the industry's standard dummy text</p><a class="btn" href="#">Read More</a></article>
    <article class="recipe-card"><div class="photo p3" role="img" aria-label="Sausages, fried eggs, mushrooms and tomatoes on a plate"></div><div class="meta"><span>By: Auther Name</span><span>2 Comments</span></div><h3>Lorem Ipsum is simply dummy text of the printing and typesetting industry.</h3><p>Lorem Ipsum is simply dummy text of the printing and typesetting industry. Lorem Ipsum has been the industry's standard dummy text</p><a class="btn" href="#">Read More</a></article>
    <article class="recipe-card"><div class="photo p4" role="img" aria-label="Grilled chicken with vegetables on a white plate"></div><div class="meta"><span>By: Auther Name</span><span>2 Comments</span></div><h3>Lorem Ipsum is simply dummy text of the printing and typesetting industry.</h3><p>Lorem Ipsum is simply dummy text of the printing and typesetting industry. Lorem Ipsum has been the industry's standard dummy text</p><a class="btn" href="#">Read More</a></article>
    <article class="recipe-card"><div class="photo p5" role="img" aria-label="Full breakfast with eggs, bacon, toast and beans on a wooden table"></div><div class="meta"><span>By: Auther Name</span><span>2 Comments</span></div><h3>Lorem Ipsum is simply dummy text of the printing and typesetting industry.</h3><p>Lorem Ipsum is simply dummy text of the printing and typesetting industry. Lorem Ipsum has been the industry's standard dummy text</p><a class="btn" href="#">Read More</a></article>
    <article class="recipe-card"><div class="photo p6" role="img" aria-label="Pastries, dips, olives and tea spread on a wooden board"></div><div class="meta"><span>By: Auther Name</span><span>2 Comments</span></div><h3>Lorem Ipsum is simply dummy text of the printing and typesetting industry.</h3><p>Lorem Ipsum is simply dummy text of the printing and typesetting industry. Lorem Ipsum has been the industry's standard dummy text</p><a class="btn" href="#">Read More</a></article>
  </div>
  <a class="btn more" href="#">Explore More <span class="dot"><svg width="8" height="8" viewBox="0 0 8 8"><path d="M2.5 1l3 3-3 3" fill="none" stroke="#5b8a0e" stroke-width="1.6"/></svg></span></a>
</section>

<footer class="site-footer">
  <div class="fcol contact" style="left:115px">
    <h4>Contact Us</h4>
    <ul>
      <li><svg width="13" height="17" viewBox="0 0 13 17"><path d="M6.5 16S1 9.5 1 6a5.5 5.5 0 0 1 11 0c0 3.5-5.5 10-5.5 10z" fill="none" stroke="#5b8a0e" stroke-width="1.5"/><circle cx="6.5" cy="6" r="2" fill="#5b8a0e"/></svg><span>27 Millstone Lane #4B<br>Ovenfield 40217</span></li>
      <li><svg width="16" height="16" viewBox="0 0 16 16"><path d="M3 1l3 3-1.5 2a9 9 0 0 0 5.5 5.5L12 10l3 3-2 2C7 15 1 9 1 3z" fill="#5b8a0e"/></svg><span>(919) 000-0000</span></li>
      <li><svg width="16" height="12" viewBox="0 0 16 12"><rect width="16" height="12" fill="#5b8a0e"/><path d="M0 0l8 6 8-6" fill="none" stroke="#fff" stroke-width="1.3"/></svg><span>name@mailbox.net</span></li>
    </ul>
  </div>
  <div class="fcol" style="left:407px"><h4>QUICK LINKS</h4><a href="#">Home</a><a href="#">About</a><a href="#">Products</a><a href="#">Shop</a></div>
  <div class="fcol" style="left:608px"><h4>QUICK LINKS</h4><a href="#">Gallery</a><a href="#">Contact Us</a><a href="#">Tearms</a></div>
  <div class="fcol newsletter" style="left:815px"><h4>WRITE TO US</h4><p>Provide your email below to subscribe to our newsletter</p><div class="subscribe"><span>Email address</span><b>Subscribe</b></div></div>
  <div class="footer-rule"></div>
  <div class="copyright">Copyright 2020 Company Name.&nbsp; All Rights Reserved.</div>
  <div class="social"><span></span><span></span><span></span></div>
</footer>

</body>
</html>
```